Coffee Bag Label

I need a coffee bag label designed (front label and back label):
Our company "Tidy-Pod" imports organic coffee beans direct from a farm on Vorsela Mountain on a private reserve (rainforest) from Jinotega, Nicaragua.
Labels should each be 3 inches x 3 inches (with room on edges for bleed). I want the front label to catch the eye and coordinate well with the coffee bag. The bags sizes are below and pictures are attached.
Bag sizes: Lime green 12 oz bag: 3-3/8" x 2-9/16" x 10-1/4"
Black 2 oz sample stand up pouch: 4" x 6-1/2" + 2-3/8", 2oz (60g)
Black 2lb bag: 5" x 3-3/8" x 15", 2lb (1kg)
Please include as much as possible below on the front label without it looking too wordy:
1) Our logo (it's attached). Feel free to do something creative with just the bean and place "Tidy-Pod" or "Tidy-Pod Coffees" somewhere else. They don't have to be together like in the attached file. The bean can be in the background of the label as well or something else cool like in the form of a cloud over the volcano or as the sun in the sky over the volcano.
2) lime green, burnt orange, dark brown & black
3) Front label should say:
"100% Premium Arabica Nicaraguan Coffee"
"Organic, Rain Forest & Mountain Shade Grown"
Bottom of label:
"Medium Roast"
"Full body, bold flavor, nutty, hints of chocolate, with a distinct & flavorful aroma."
I want one front label file for each size bag: "2 oz" "12 oz" & "32 oz"
Back of the label:
I have uploaded a hand drawn pic of what I am thinking but if you have a better idea please submit it.
Please include as much as possible below without it looking wordy:
Directions on the perfect cup:
***2 Tbsp high quality coffee 6 Oz. cup of pure filtered water
(these can be tied into the hand-drawn picture. I will label the section each one corresponds to)
Organically Grown (sustainable)
Rainforest Grown (sustainable)
Mountain Shade Grown (sustainable)
Hand Picked (select)
Spring Water Washed (select)
Sun Dried (select)
Social Responsibility (profits help fund Bright Path Outreach Nicaragua www.brightpathoutreach.example.org)
Single Source Coffee (Single source)
Traceable Source (single source)
Website: www.Tidy-Pod.example.com
Reason: I have been asked to extend deadline by a few designers.
Thanks,
Joanne Pelter
ages 18-54
- Should have a cool border. Maybe fade from one color to another or have something more original than just a 3x3 square border.

```html
<!DOCTYPE html>
<html lang="en">
<head>
<meta charset="utf-8">
<title>Tidy-Pod Nicaraguan Coffee Labels</title>
<link href="https://fonts.googleapis.com/css2?family=Parisienne&family=Pathway+Gothic+One&family=Playfair+Display+SC:wght@700&family=Special+Elite&display=swap" rel="stylesheet">
<style>
  :root {
    --lime: #a3cd7e;
    --brown-deep: #1e0f07;
    --brown-mid: #4a2a17;
    --brown-line: #7a5230;
    --leaf-green: #93c46a;
    --burnt-orange: #e6953a;
    --cream: #f3ece2;
    --caption: #ffffff;
  }
  * { margin: 0; padding: 0; box-sizing: border-box; }
  html, body { width: 1200px; height: 760px; overflow: hidden; }
  body {
    background: var(--lime);
    font-family: "Pathway Gothic One", "Arial Narrow", sans-serif;
    color: var(--cream);
    position: relative;
  }
  .label {
    position: absolute;
    top: 170px;
    width: 510px;
    height: 510px;
  }
  .label--front { left: 70px; }
  .label--back { left: 620px; }
  .label__shape { position: absolute; inset: 0; }
  .label__caption {
    position: absolute;
    top: -70px;
    left: 330px;
    font-family: "Pathway Gothic One", sans-serif;
    font-size: 26px;
    letter-spacing: 1px;
    color: var(--caption);
    white-space: nowrap;
  }
  .label__content {
    position: absolute;
    inset: 0;
    text-align: center;
  }
  .line { position: absolute; left: 0; right: 0; white-space: nowrap; }
  .cup-mark {
    position: absolute;
    left: 246px;
    width: 18px;
    height: 14px;
    background: var(--burnt-orange);
    border-radius: 0 0 9px 9px;
  }
  .origin {
    font-family: "Playfair Display SC", serif;
    font-weight: 700;
    font-size: 21px;
    letter-spacing: 3px;
    color: var(--leaf-green);
  }
  .origin--small { font-size: 18px; }
  .product-name {
    font-family: "Parisienne", cursive;
    font-size: 84px;
    line-height: 1;
    color: var(--cream);
  }
  .bean-cluster {
    position: absolute;
    left: 362px;
    top: 240px;
    width: 38px;
    height: 24px;
    border-radius: 50%;
    background: radial-gradient(ellipse at center, #b97836, #8a5424);
  }
  .roast {
    font-family: "Playfair Display SC", serif;
    font-weight: 700;
    font-size: 15px;
    letter-spacing: 3px;
    color: var(--leaf-green);
  }
  .tasting {
    font-size: 15px;
    letter-spacing: 1px;
    line-height: 19px;
    text-transform: uppercase;
  }
  .brand-name {
    font-family: "Pathway Gothic One", sans-serif;
    font-size: 28px;
    letter-spacing: 1px;
    color: var(--burnt-orange);
  }
  .net-weight { font-size: 13px; letter-spacing: 1px; }
  .growing {
    font-size: 14px;
    letter-spacing: 1px;
    text-transform: uppercase;
  }
  .directions-title {
    font-family: "Playfair Display SC", serif;
    font-weight: 700;
    font-size: 17px;
    letter-spacing: 2px;
    color: var(--leaf-green);
  }
  .directions-step {
    font-size: 15px;
    letter-spacing: 2px;
    text-transform: uppercase;
  }
  .attribute-row {
    display: flex;
    justify-content: center;
    gap: 20px;
    font-size: 13px;
    letter-spacing: 1px;
    text-transform: uppercase;
  }
  .arc-text {
    font-family: "Special Elite", monospace;
    font-size: 11px;
    letter-spacing: 2px;
    fill: var(--cream);
  }
</style>
</head>
<body>

<section class="label label--front" aria-label="Front label">
  <p class="label__caption">FRONT LABEL</p>
  <svg class="label__shape" viewBox="0 0 510 510">
    <defs>
      <radialGradient id="front-fill" cx="50%" cy="50%" r="55%">
        <stop offset="0%" stop-color="var(--brown-mid)"/>
        <stop offset="100%" stop-color="var(--brown-deep)"/>
      </radialGradient>
      <path id="front-arc" d="M 150 150 Q 255 95 360 150"/>
    </defs>
    <polygon points="255,0 510,255 255,510 0,255" fill="url(#front-fill)"/>
    <polygon points="255,28 482,255 255,482 28,255" fill="none" stroke="var(--brown-line)" stroke-width="2"/>
    <polygon points="255,40 470,255 255,470 40,255" fill="none" stroke="var(--brown-line)" stroke-width="1"/>
    <text class="arc-text"><textPath href="#front-arc" startOffset="50%" text-anchor="middle">100% PREMIUM ARABICA</textPath></text>
  </svg>
  <div class="label__content">
    <span class="cup-mark" style="top:138px" role="img" aria-label="Small coffee cup icon"></span>
    <p class="line origin" style="top:162px">Nicaraguan</p>
    <p class="line product-name" style="top:198px">Coffee</p>
    <span class="bean-cluster" role="img" aria-label="Cluster of coffee beans"></span>
    <p class="line roast" style="top:308px">Medium Roast</p>
    <p class="line tasting" style="top:334px">Full body, bold flavor, nutty, hints of chocolate,<br>with a distinct &amp; flavorful aroma.</p>
    <p class="line brand-name" style="top:386px">Tidy-Pod</p>
    <p class="line net-weight" style="top:440px">12 oz</p>
  </div>
</section>

<section class="label label--back" aria-label="Back label">
  <p class="label__caption">BACK LABEL</p>
  <svg class="label__shape" viewBox="0 0 510 510">
    <defs>
      <radialGradient id="back-fill" cx="50%" cy="50%" r="55%">
        <stop offset="0%" stop-color="var(--brown-mid)"/>
        <stop offset="100%" stop-color="var(--brown-deep)"/>
      </radialGradient>
      <path id="back-arc" d="M 150 130 Q 255 75 360 130"/>
    </defs>
    <polygon points="255,0 510,255 255,510 0,255" fill="url(#back-fill)"/>
    <polygon points="255,28 482,255 255,482 28,255" fill="none" stroke="var(--brown-line)" stroke-width="2"/>
    <polygon points="255,40 470,255 255,470 40,255" fill="none" stroke="var(--brown-line)" stroke-width="1"/>
    <text class="arc-text"><textPath href="#back-arc" startOffset="50%" text-anchor="middle">100% PREMIUM ARABICA</textPath></text>
  </svg>
  <div class="label__content">
    <span class="cup-mark" style="top:116px" role="img" aria-label="Small coffee cup icon"></span>
    <p class="line origin origin--small" style="top:134px">Nicaraguan</p>
    <p class="line growing" style="top:160px">Organic, Rain Forest &amp; Mountain Shade Grown</p>
    <p class="line directions-title" style="top:196px">Directions on the Perfect Cup:</p>
    <p class="line directions-step" style="top:222px">***2 Tbsp high quality coffee</p>
    <p class="line directions-step" style="top:242px">6 Oz. cup of pure filtered water</p>
    <div class="line attribute-row" style="top:278px"><span>Organically Grown</span><span>Rainforest Grown</span><span>Mountain Shade Grown</span></div>
    <div class="line attribute-row" style="top:297px"><span>Hand Picked</span><span>Spring Water Washed</span><span>Sun Dried</span></div>
    <div class="line attribute-row" style="top:316px"><span>Growers with Social Responsibility</span></div>
    <div class="line attribute-row" style="top:335px"><span>Single Source Coffee</span><span>Traceable Source</span></div>
    <p class="line brand-name" style="top:386px">Tidy-Pod</p>
  </div>
</section>

</body>
</html>
```